Private Equity Fund needs a powerpoint template

We need a power point presentation template for our recent founded firm, Corvane Partners, a private equity/investment fund (funded by investors, is a firm that buys, holds and sells companies years after) focused in turnaround cases. The presentation should address corporate and financial subjects in a clean/plain way, but as most straightforward way as possible. This is a commercial pitch/flip presentation, is not a presentation with animations to be presented to a mass of people.

We would like that the designer resume the file that we began building (adapted from other funds/advisors of the market) and establish the following according to our logo:
1) a new set of fonts (size levels and type),
2) colors (tables, headers, lines),
3) space available for content (text boxes, tables, pictures or charts) (note left column space in blank)
4) set, our Excel applications to use as default, the color guide that you have you defined
5) white background

Basically, we need to change the items listed above to the "Example.ppt" file uploaded along with those instructions.

The presentation should:
A) rule how the people in our organization should address our messages (guide with size of tables, font and size, colors)
B) pattern a set of slides that could minimize the time for arranging formats, worrying only about the content
C) allow the person who is building the presentation to have options while addressing the message

Dont get too restricted to what we are giving you (the "Example.ppt" file). You may suggest:
i) logo positioning
ii) with or without any vague space (left column space in blank)
iii) space optmization
iv) shades and colors
v) fonts (careful with the wide ones as it does not optimizes space)

I'm uploading:

Target Market(s)

Banks
Investors
Company owners/founders
Funds

Industry/Entity Type

Financial Service

Font styles to use
Other font styles liked:
• Arial Narrow, Arial, trojan

Colors

Designer to choose colors to be used in the design.

Requirements
Must have
• We would like that the designer resume the file that we began building (adapted from other funds/advisors of the market) and establish the following according to our logo:
• 1) a new set of fonts (size levels and type),
• 2) colors (tables, headers, lines),
• 3) space available for content (text boxes, tables, pictures or charts) (note left column space in blank)
• 4) set, our Excel applications to use as default, the color guide that you have you defined
• 5) white background
Nice to have
• Narrow font type
• Space optimization
• Discrete
Should not have
• Animations
• Font size too big
• colored background

```html
<!DOCTYPE html>
<html lang="en">
<head>
<meta charset="utf-8">
<title>Corvane Partners – Presentation Template</title>
<link rel="stylesheet" href="https://fonts.googleapis.com/css2?family=PT+Sans+Narrow:wght@400;700&family=Roboto+Condensed:wght@400;700&display=swap">
<style>
:root{
  --stage:#bcbcbc;
  --paper:#ffffff;
  --brand:#7a88b0;
  --strip:#8c99bf;
  --strip-soft:#e4e4e6;
  --band:#a8b6cc;
  --bar:#a9b9cf;
  --bar-soft:#e8ebf1;
  --slate:#6f84a4;
  --sky:#b7c5d9;
  --green:#a6d58c;
  --olive:#dfe59f;
  --yellow:#f6d98c;
  --tan:#cbbfb5;
  --ink:#555a63;
  --muted:#8a8f98;
  --rule:#c9ced8;
}
*{box-sizing:border-box;margin:0;padding:0}
html,body{width:1200px;height:850px;overflow:hidden;background:var(--stage)}
body{font-family:"Roboto Condensed",Arial,sans-serif;color:var(--ink);position:relative}
.slide{position:absolute;width:388px;height:270px;background:var(--paper);box-shadow:0 1px 4px rgba(0,0,0,.35);overflow:hidden}
.slide::before{content:"";position:absolute;left:0;top:0;bottom:0;width:8px;background:var(--strip)}
.c1{left:10px}.c2{left:406px}.c3{left:802px}
.r1{top:14px}.r2{top:290px}.r3{top:566px}
.slide-title{position:absolute;left:20px;top:5px;font-family:"PT Sans Narrow",sans-serif;font-weight:700;font-size:14px;color:var(--brand)}
.slide-sub{position:absolute;left:20px;top:21px;font-size:5.5px;color:var(--muted)}
.page-no{position:absolute;right:8px;top:6px;width:12px;height:13px;background:var(--strip);color:#fff;font-size:5.5px;font-weight:700;text-align:center;line-height:11px;clip-path:polygon(0 0,100% 0,100% 78%,50% 100%,0 78%)}
.footer-mark{position:absolute;left:13px;bottom:6px;display:flex;align-items:center;gap:3px;font-family:"PT Sans Narrow",sans-serif;font-size:9px;letter-spacing:.6px;color:#5d6068}
.footer-mark i{width:7px;height:7px;background:#5d6068;display:block}
/* cover */
.cover::after{content:"";position:absolute;left:8px;top:0;bottom:0;width:10px;background:var(--strip-soft)}
.cover-brand{position:absolute;left:28px;display:flex;align-items:center;gap:4px;font-family:"PT Sans Narrow",sans-serif;font-size:15px;letter-spacing:.8px;color:#4f535b;line-height:16px}
.cover-brand i{width:13px;height:13px;background:#4f535b;display:block}
.cover-title{position:absolute;left:28px;font-family:"PT Sans Narrow",sans-serif;font-weight:700;font-size:13px;line-height:14px;color:var(--brand)}
.cover-sub{position:absolute;left:28px;font-family:"PT Sans Narrow",sans-serif;font-size:8px;line-height:9px;color:var(--sky)}
/* contents */
.toc{position:absolute;left:66px;top:86px;width:250px}
.toc-row{display:flex;align-items:center;height:16.5px;border-bottom:1px solid #e4e6eb;font-size:5.5px;color:var(--muted)}
.toc-no{width:25px;height:16px;background:var(--band);color:#fff;font-weight:700;font-size:6px;text-align:center;line-height:16px;margin-right:12px}
.toc-label{flex:1}
.toc-page{width:30px}
/* disclaimer */
.legal{position:absolute;left:16px;right:18px;top:40px;font-size:4.2px;line-height:6.3px;color:#333;text-align:justify;text-transform:uppercase}
.legal p{margin-bottom:4px}
/* highlight banner */
.banner{position:absolute;left:13px;right:3px;top:56px;height:45px;background:var(--band);border:2px solid #d6dde8;display:flex}
.banner-item{flex:1;display:flex;align-items:center;gap:8px;padding-left:16px;color:#fff}
.banner-item b{display:block;font-family:"PT Sans Narrow",sans-serif;font-size:10px}
.banner-item span{display:block;font-size:4.5px;opacity:.85;line-height:5.5px}
.note{position:absolute;display:flex;gap:8px;font-size:5px;line-height:6.5px;color:var(--muted)}
.note b{color:#333}
.doc-icon{flex:none}
/* headers */
.band-head{position:absolute;height:13px;background:var(--band);color:#fff;font-family:"PT Sans Narrow",sans-serif;font-weight:700;font-size:7px;text-align:center;line-height:13px}
.desc{position:absolute;font-size:4.3px;line-height:5.5px;color:var(--muted)}
.desc h4{font-weight:400;font-size:6px;color:var(--slate);margin-bottom:2px}
.desc .kpi{float:left;font-family:"PT Sans Narrow",sans-serif;font-weight:700;font-size:15px;line-height:14px;margin-right:5px}
.kpi.green{color:#7dc45b}.kpi.yellow{color:#f1c24a}
/* pies */
.pie-card{position:absolute;top:40px;width:106px}
.pie-box{height:95px;background:#fbfbfd;border:1px solid #e8eaef;position:relative}
.pie-box svg{position:absolute;left:24px;top:13px}
.pie-lbl{position:absolute;font-size:5.5px;color:#555}
.pie-cap{height:11px;background:var(--band);color:#fff;font-family:"PT Sans Narrow",sans-serif;font-weight:700;font-size:7px;text-align:center;line-height:11px}
.pie-src{font-size:4.5px;text-align:center;color:var(--muted);margin:2px 0}
.pie-list{list-style:none;border:1px solid #eceef2;padding:3px 4px;font-size:4.3px;line-height:6px;color:var(--muted);height:50px}
.pie-list li::before{content:"\25B6";font-size:3px;color:var(--slate);margin-right:3px;vertical-align:1px}
/* team */
.board{position:absolute;left:88px;top:40px;width:220px;font-size:4.5px;color:#333}
.board h5{text-align:center;font-weight:400;font-size:5px;margin-bottom:2px}
.board table{width:100%;border-collapse:collapse}
.board td{border:1px solid #cfd3da;padding:1px 3px;line-height:5.5px;vertical-align:top}
.board td:first-child{width:60px;text-align:right}
.task-head{position:absolute;left:16px;right:10px;top:86px;border-top:1px solid #555;padding-top:1px;text-align:center;font-weight:700;font-size:4.8px;color:#333}
.team{position:absolute;left:16px;right:10px;top:95px;display:grid;grid-template-columns:repeat(5,1fr);gap:4px}
.team h6{font-weight:400;font-size:5px;color:#333;border-bottom:1px solid #555;padding-bottom:1px;margin-bottom:3px}
.team ul{list-style:none;font-size:4.2px;line-height:5px;color:var(--muted)}
.team li{margin-bottom:6px;padding-left:5px;position:relative}
.team li::before{content:"";position:absolute;left:0;top:2px;width:2px;height:2px;background:var(--slate)}
.axis{font-size:5px;fill:#777;font-family:"Roboto Condensed",sans-serif}
</style>
</head>
<body>

<svg width="0" height="0" style="position:absolute" aria-hidden="true">
  <defs>
    <symbol id="pie" viewBox="0 0 42 42">
      <g transform="rotate(-90 21 21)" fill="none" stroke-width="21">
        <circle cx="21" cy="21" r="10.5" pathLength="100" stroke="#cbbfb5" stroke-dasharray="8 100" stroke-dashoffset="0"/>
        <circle cx="21" cy="21" r="10.5" pathLength="100" stroke="#a6d58c" stroke-dasharray="25 100" stroke-dashoffset="-8"/>
        <circle cx="21" cy="21" r="10.5" pathLength="100" stroke="#cfe29c" stroke-dasharray="20 100" stroke-dashoffset="-33"/>
        <circle cx="21" cy="21" r="10.5" pathLength="100" stroke="#f6d98c" stroke-dasharray="15 100" stroke-dashoffset="-53"/>
        <circle cx="21" cy="21" r="10.5" pathLength="100" stroke="#b7c5d9" stroke-dasharray="12 100" stroke-dashoffset="-68"/>
        <circle cx="21" cy="21" r="10.5" pathLength="100" stroke="#7389a8" stroke-dasharray="20 100" stroke-dashoffset="-80"/>
      </g>
    </symbol>
    <symbol id="doc" viewBox="0 0 20 24">
      <path d="M2 1h11l5 5v17H2z" fill="none" stroke="#9fd07a" stroke-width="1.6"/>
      <path d="M13 1v5h5M5 11h10M5 15h10M5 19h10" fill="none" stroke="#9fd07a" stroke-width="1.4"/>
    </symbol>
  </defs>
</svg>

<!-- 1 Cover -->
<section class="slide c1 r1 cover">
  <div class="cover-brand" style="top:196px"><i></i>CORVANE PARTNERS</div>
  <div class="cover-title" style="top:218px">PRIVATE EQUITY FUND</div>
  <div class="cover-sub" style="top:234px">Financial Services</div>
</section>

<!-- 2 Contents -->
<section class="slide c2 r1">
  <h1 class="slide-title">Contents</h1>
  <div class="page-no">2</div>
  <div class="toc">
    <div class="toc-row"><span class="toc-no">01</span><span class="toc-label">Quisque commodo lacus sed lectus</span><span class="toc-page">03</span></div>
    <div class="toc-row"><span class="toc-no">02</span><span class="toc-label">Aenean ultricies eu orci</span><span class="toc-page">06</span></div>
    <div class="toc-row"><span class="toc-no">03</span><span class="toc-label">Lorem ipsum dolor sit amet</span><span class="toc-page">12</span></div>
    <div class="toc-row"><span class="toc-no">04</span><span class="toc-label">Aenean ultricies eu orci</span><span class="toc-page">18</span></div>
    <div class="toc-row"><span class="toc-no">05</span><span class="toc-label">Quisque commodo lacus sed lectus</span><span class="toc-page">24</span></div>
    <div class="toc-row"><span class="toc-no">06</span><span class="toc-label">Lorem ipsum dolor sit amet</span><span class="toc-page">28</span></div>
  </div>
  <div class="footer-mark"><i></i>CORVANE</div>
</section>

<!-- 3 Disclaimer -->
<section class="slide c3 r1">
  <h1 class="slide-title">1.1 DISCLAIMER</h1>
  <div class="page-no">3</div>
  <div class="legal">
    <p>This confidential concept deck has been prepared solely for, and is being delivered on a confidential basis to, prospective investors considering the purchase of limited partnership interests in Corvane Partners Fund I, L.P. (the "Fund"). The Fund will be managed by Halvern Capital Advisors, L.L.C. Each recipient agrees to keep all information contained herein confidential and to use it for the sole purpose of evaluating a possible investment in the Fund.</p>
    <p>Restrictions on solicitations</p>
    <p>This concept deck does not constitute an offer to sell or a solicitation of an offer to buy the securities described herein in any state or other jurisdiction in which such offer is unlawful.</p>
    <p>Investors should be aware that they may be required to bear the financial risks of their investment for an indefinite period of time. Investment in the securities will involve significant risks due to, among other things, the nature of the Fund's investments. Investors should have the financial ability and willingness to accept the risks and lack of liquidity that are characteristic of the investment described herein.</p>
    <p>In making an investment decision, each investor must rely on its own examination of the Fund and the actual terms of any offering. All of the statements and information contained in this deck are subject to and qualified in their entirety by reference to the Fund offering and operative documents. In the event that the descriptions herein are inconsistent with those documents, the operative documents shall control.</p>
    <p>Forward looking statements</p>
    <p>This concept deck contains forward looking statements that relate to the financial and regulatory environments in which the Fund will operate and various other matters, such as certain financial projections and assumptions concerning hypothetical rates of return and standard deviations. These projections and assumptions reflect a number of assumptions concerning expected market conditions, types of investment opportunities and the like. Words such as "anticipate", "estimate", "project", "plan", "intend", "expect", "believe" and similar expressions identify such statements. Actual results and events could differ materially from those contemplated. There can be no assurance that the Fund's objectives will be achieved or that investors will receive a return of their capital. The Fund does not undertake any obligation publicly to update or revise any forward looking statement.</p>
  </div>
  <div class="footer-mark"><i></i>CORVANE</div>
</section>

<!-- 4 Executive summary -->
<section class="slide c1 r2 cover">
  <div class="cover-brand" style="top:194px"><i></i>CORVANE PARTNERS</div>
  <div class="cover-title" style="top:216px">EXECUTIVE SUMMARY</div>
</section>

<!-- 5 Standard width -->
<section class="slide c2 r2">
  <h1 class="slide-title">Standard width layout</h1>
  <p class="slide-sub">Maecenas sem eros, luctus quis facilisis in, tristique sit amet erat.</p>
  <div class="page-no">5</div>
  <div class="banner">
    <div class="banner-item">
      <svg width="14" height="16" viewBox="0 0 14 16"><path d="M7 0 14 7H9.5v9h-5V7H0z" fill="#fff"/></svg>
      <div><b>68% INCREASE</b><span>Phasellus maximus<br>mauris at pulvinar mollis.</span></div>
    </div>
    <div class="banner-item">
      <svg width="22" height="14" viewBox="0 0 22 14"><path d="M2 13A9 9 0 0 1 20 13" fill="none" stroke="#fff" stroke-width="3" stroke-dasharray="2 1.2"/><path d="M11 13 15 5" stroke="#f3c64a" stroke-width="1.6"/></svg>
      <div><b>ACCELERATE</b><span>Phasellus maximus<br>mauris at pulvinar mollis.</span></div>
    </div>
    <div class="banner-item">
      <svg width="18" height="14" viewBox="0 0 18 14"><path d="M1 13h16" stroke="#fff"/><rect x="2" y="8" width="2.5" height="5" fill="#fff"/><rect x="6" y="5" width="2.5" height="8" fill="#fff"/><rect x="10" y="7" width="2.5" height="6" fill="#fff"/><rect x="14" y="2" width="2.5" height="11" fill="#fff"/></svg>
      <div><b>REPORT</b><span>Phasellus maximus<br>mauris at pulvinar mollis.</span></div>
    </div>
  </div>
  <svg style="position:absolute;left:15px;top:105px" width="365" height="122" viewBox="0 0 365 122">
    <g class="axis" text-anchor="end">
      <text x="30" y="112">0</text><text x="30" y="95.5">20</text><text x="30" y="78.8">40</text><text x="30" y="62">60</text><text x="30" y="45.5">80</text><text x="30" y="28.8">100</text><text x="30" y="12">120</text>
    </g>
    <path d="M36 110H362" stroke="#999" stroke-width=".5"/>
    <g fill="var(--bar)">
      <rect x="45" y="26.7" width="8" height="83.3"/><rect x="71.7" y="35" width="8" height="75"/><rect x="98.3" y="68.3" width="8" height="41.7"/><rect x="125" y="26.7" width="8" height="83.3"/><rect x="151.7" y="26.7" width="8" height="83.3"/><rect x="178.3" y="60" width="8" height="50"/><rect x="205" y="68.3" width="8" height="41.7"/><rect x="231.7" y="43.3" width="8" height="66.7"/><rect x="258.3" y="85" width="8" height="25"/><rect x="285" y="51.7" width="8" height="58.3"/><rect x="311.7" y="26.7" width="8" height="83.3"/><rect x="338.3" y="68.3" width="8" height="41.7"/>
    </g>
    <g fill="var(--bar-soft)">
      <rect x="54" y="35" width="8" height="75"/><rect x="80.7" y="43.3" width="8" height="66.7"/><rect x="107.3" y="26.7" width="8" height="83.3"/><rect x="134" y="60" width="8" height="50"/><rect x="160.7" y="30.8" width="8" height="79.2"/><rect x="187.3" y="47.5" width="8" height="62.5"/><rect x="214" y="26.7" width="8" height="83.3"/><rect x="240.7" y="60" width="8" height="50"/><rect x="267.3" y="55.8" width="8" height="54.2"/><rect x="294" y="43.3" width="8" height="66.7"/><rect x="320.7" y="26.7" width="8" height="83.3"/><rect x="347.3" y="26.7" width="8" height="83.3"/>
    </g>
    <g class="axis" text-anchor="middle">
      <text x="53" y="119">Jan</text><text x="80" y="119">Feb</text><text x="107" y="119">Mar</text><text x="133" y="119">Apr</text><text x="160" y="119">May</text><text x="187" y="119">Jun</text><text x="213" y="119">Jul</text><text x="240" y="119">Aug</text><text x="267" y="119">Sep</text><text x="293" y="119">Oct</text><text x="320" y="119">Nov</text><text x="347" y="119">Dec</text>
    </g>
  </svg>
  <div class="note" style="left:80px;top:230px;width:280px">
    <svg class="doc-icon" width="16" height="20"><use href="#doc"/></svg>
    <p><b>Quisque libero purus, bibendum nec quam sit amet, porta interdum ex.</b> Aliquam erat volutpat. Quisque commodo lacus sed lectus condimentum cursus. Praesent a diam neque. Aenean ultricies eu orci id euismod. Integer eleifend, lacus quis tincidunt posuere, nisl neque sodales justo, quis suscipit libero odio ut quam.</p>
  </div>
  <div class="footer-mark"><i></i>CORVANE</div>
</section>

<!-- 6 Two column -->
<section class="slide c3 r2">
  <h1 class="slide-title">2 Two column layout</h1>
  <div class="page-no">6</div>
  <svg style="position:absolute;left:14px;top:48px" width="180" height="140" viewBox="0 0 180 140">
    <g class="axis" text-anchor="end"><text x="14" y="130">0</text><text x="14" y="113">20</text><text x="14" y="96">40</text><text x="14" y="79">60</text><text x="14" y="62">80</text><text x="14" y="45">100</text><text x="14" y="28">120</text></g>
    <path d="M18 127H175" stroke="#999" stroke-width=".5"/>
    <rect x="24" y="42" width="8" height="85" fill="#7d8fae"/>
    <rect x="44" y="50.5" width="8" height="76.5" fill="#b4c3d8"/>
    <rect x="64" y="84.5" width="8" height="42.5" fill="#dfe59f"/>
    <rect x="84" y="42" width="8" height="85" fill="#a6d58c"/>
    <rect x="104" y="42" width="8" height="85" fill="#f6d98c"/>
    <rect x="124" y="76" width="8" height="51" fill="#cbbfb5"/>
    <rect x="144" y="84.5" width="8" height="42.5" fill="#dbe2ee"/>
    <rect x="164" y="59" width="8" height="68" fill="#e3e3e3"/>
    <g class="axis" text-anchor="middle" style="font-size:4px"><text x="28" y="135">Jan</text><text x="48" y="135">Feb</text><text x="68" y="135">Mar</text><text x="88" y="135">Apr</text><text x="108" y="135">May</text><text x="128" y="135">Jun</text><text x="148" y="135">Jul</text><text x="168" y="135">Aug</text></g>
  </svg>
  <svg style="position:absolute;left:200px;top:45px" width="185" height="135" viewBox="0 0 185 135">
    <g class="axis" text-anchor="end" style="font-size:4px"><text x="16" y="124">0%</text><text x="16" y="108">20%</text><text x="16" y="92">40%</text><text x="16" y="76">60%</text><text x="16" y="60">80%</text><text x="16" y="44">100%</text></g>
    <g class="axis" style="font-size:4px"><text x="165" y="124">$0.00</text><text x="165" y="110">$5.00</text><text x="165" y="97">$10.00</text><text x="165" y="84">$15.00</text><text x="165" y="70">$20.00</text><text x="165" y="57">$25.00</text><text x="165" y="44">$30.00</text></g>
    <g>
      <rect x="30" y="102" width="24" height="20" fill="#7389a8"/><rect x="30" y="86" width="24" height="16" fill="#b7c5d9"/><rect x="30" y="72" width="24" height="14" fill="#a6d58c"/><rect x="30" y="42" width="24" height="30" fill="#dfe59f"/>
      <rect x="76" y="95" width="24" height="27" fill="#7389a8"/><rect x="76" y="86" width="24" height="9" fill="#b7c5d9"/><rect x="76" y="66" width="24" height="20" fill="#a6d58c"/><rect x="76" y="42" width="24" height="24" fill="#dfe59f"/>
      <rect x="122" y="95" width="24" height="27" fill="#7389a8"/><rect x="122" y="76" width="24" height="19" fill="#b7c5d9"/><rect x="122" y="62" width="24" height="14" fill="#a6d58c"/><rect x="122" y="42" width="24" height="20" fill="#dfe59f"/>
    </g>
    <g fill="#fff" font-size="3.6" text-anchor="middle" font-family="Roboto Condensed,sans-serif"><text x="42" y="114">12.5</text><text x="88" y="110">17</text><text x="134" y="110">22</text></g>
    <path d="M42 72Q88 40 134 80" fill="none" stroke="#f1b83a" stroke-width="1"/>
    <g class="axis" text-anchor="middle" style="font-size:4px"><text x="42" y="130">Jan</text><text x="88" y="130">Feb</text><text x="134" y="130">Mar</text></g>
  </svg>
  <div style="position:absolute;left:262px;top:181px;font-size:3.6px;color:#888;white-space:nowrap">■ Air &nbsp; ■ Budget &nbsp; ■ Banners &nbsp; ■ Binding &nbsp; — Price</div>
  <div class="band-head" style="left:12px;top:193px;width:186px">Some title here</div>
  <div class="band-head" style="left:200px;top:193px;width:186px">Some title here</div>
  <div class="desc" style="left:18px;top:212px;width:175px">
    <h4>Description Here</h4>
    <p><span class="kpi green">80%</span>There are many of the variations passages lorem ipsum available majority have suffered but the have suffered alteration in some.</p>
    <p style="clear:both;margin-top:2px">There are many variations of passages of Lorem Ipsum available, but the have suffered alteration in some form, by humour, or randomised words which don't believable.</p>
  </div>
  <div class="desc" style="left:204px;top:212px;width:175px">
    <h4>Description Here</h4>
    <p><span class="kpi yellow">20%</span>There are many of the variations passages lorem ipsum available majority have suffered but the have suffered alteration in some.</p>
    <p style="clear:both;margin-top:2px">There are many variations of passages of Lorem Ipsum available, but the have suffered alteration in some form, by humour, or randomised words which don't believable.</p>
  </div>
  <div class="footer-mark"><i></i>CORVANE</div>
</section>

<!-- 7 Three columns -->
<section class="slide c1 r3">
  <h1 class="slide-title">3 Three columns layout</h1>
  <p class="slide-sub">Maecenas sem eros, luctus quis facilisis in, tristique sit amet erat.</p>
  <div class="page-no">7</div>
  <div class="pie-card" style="left:24px">
    <div class="pie-box"><svg width="62" height="62"><use href="#pie"/></svg>
      <span class="pie-lbl" style="left:62px;top:4px">8%</span><span class="pie-lbl" style="left:88px;top:30px">25%</span><span class="pie-lbl" style="left:70px;top:80px">20%</span><span class="pie-lbl" style="left:22px;top:75px">15%</span><span class="pie-lbl" style="left:10px;top:43px">12%</span><span class="pie-lbl" style="left:24px;top:8px">20%</span></div>
    <div class="pie-cap">Option A (Revenue 2011)</div>
    <div class="pie-src">Source Corvane 26/05/2011</div>
    <ul class="pie-list"><li>Growth limited to management capacity - some opportunities might be "lost"</li><li>Availability of suitable sites</li><li>Deterioration of UK macroeconomic environment</li><li>Geographic expansion increases risk</li></ul>
  </div>
  <div class="pie-card" style="left:141px">
    <div class="pie-box"><svg width="62" height="62"><use href="#pie"/></svg>
      <span class="pie-lbl" style="left:62px;top:4px">8%</span><span class="pie-lbl" style="left:88px;top:30px">25%</span><span class="pie-lbl" style="left:70px;top:80px">20%</span><span class="pie-lbl" style="left:22px;top:75px">15%</span><span class="pie-lbl" style="left:10px;top:43px">12%</span><span class="pie-lbl" style="left:24px;top:8px">20%</span></div>
    <div class="pie-cap">Option A (Revenue 2011)</div>
    <div class="pie-src">Source Corvane 26/05/2011</div>
    <ul class="pie-list"><li>Integration risks - management time</li><li>The 'Halden effect'</li><li>Further equity investment likely</li><li>New segment/geography unknown to management</li><li>Availability of suitable targets</li></ul>
  </div>
  <div class="pie-card" style="left:258px">
    <div class="pie-box"><svg width="62" height="62"><use href="#pie"/></svg>
      <span class="pie-lbl" style="left:62px;top:4px">8%</span><span class="pie-lbl" style="left:88px;top:30px">25%</span><span class="pie-lbl" style="left:70px;top:80px">20%</span><span class="pie-lbl" style="left:22px;top:75px">15%</span><span class="pie-lbl" style="left:10px;top:43px">12%</span><span class="pie-lbl" style="left:24px;top:8px">20%</span></div>
    <div class="pie-cap">Option A (Revenue 2011)</div>
    <div class="pie-src">Source Corvane 26/05/2011</div>
    <ul class="pie-list"><li>Debate &amp; agree key messages/themes</li><li>Construct value arguments</li><li>Prepare robust supporting data</li><li>Ensure management information systems in place to produce supporting data</li></ul>
  </div>
  <div class="note" style="left:30px;top:228px;width:350px">
    <svg class="doc-icon" width="18" height="22"><use href="#doc"/></svg>
    <p><b>Quisque libero purus, bibendum nec quam sit amet, porta interdum ex.</b> Aliquam erat volutpat. Quisque commodo lacus sed lectus condimentum cursus. Praesent a diam neque. Aenean ultricies eu orci id euismod. Integer eleifend, lacus quis tincidunt posuere, nisl neque sodales justo, quis suscipit libero odio ut quam.</p>
  </div>
  <div class="footer-mark"><i></i>CORVANE</div>
</section>

<!-- 8 Four charts -->
<section class="slide c2 r3">
  <h1 class="slide-title">4 Four charts on a page</h1>
  <p class="slide-sub">Maecenas sem eros, luctus quis facilisis in, tristique sit amet erat.</p>
  <div class="page-no">8</div>
  <div class="band-head" style="left:10px;top:34px;width:188px">Some title here</div>
  <div class="band-head" style="left:200px;top:34px;width:188px">Some title here</div>
  <svg style="position:absolute;left:14px;top:52px" width="180" height="75" viewBox="0 0 180 75">
    <g class="axis" text-anchor="end" style="font-size:3.6px"><text x="20" y="10">cards</text><text x="20" y="22">Binding</text><text x="20" y="34">Banners</text><text x="20" y="46">Budget</text><text x="20" y="58">Air</text></g>
    <rect x="83" y="6" width="38" height="5" fill="var(--bar)"/>
    <rect x="58" y="18" width="28" height="5" fill="#a6d58c"/>
    <rect x="46" y="30" width="36" height="5" fill="#dfe59f"/>
    <rect x="70" y="42" width="50" height="5" fill="#f6d98c"/>
    <rect x="50" y="54" width="34" height="5" fill="#7389a8"/>
    <path d="M24 63H170" stroke="#999" stroke-width=".4"/>
    <g class="axis" text-anchor="middle" style="font-size:3.6px"><text x="24" y="68">0</text><text x="48" y="68">10</text><text x="72" y="68">20</text><text x="97" y="68">30</text><text x="121" y="68">40</text><text x="145" y="68">50</text><text x="170" y="68">60</text></g>
    <text x="24" y="74" class="axis" style="font-size:3.4px"><tspan font-weight="700">Source</tspan> Corvane 26/05/2011</text>
  </svg>
  <svg style="position:absolute;left:205px;top:50px" width="180" height="78" viewBox="0 0 180 78">
    <g class="axis" text-anchor="end" style="font-size:3.6px"><text x="14" y="10">4%</text><text x="14" y="22">3%</text><text x="14" y="34">2%</text><text x="14" y="46">1%</text><text x="14" y="58">0%</text></g>
    <path d="M18 56 55 30 90 40 120 28 150 18 175 28V56z" fill="var(--tan)"/>
    <path d="M18 56 55 36 90 44 120 34 150 24 175 34V56z" fill="#a6d58c"/>
    <path d="M18 56 55 42 90 48 120 40 150 32 175 40V56z" fill="#f6d98c"/>
    <path d="M18 56 55 48 90 52 120 47 150 42 175 48V56z" fill="var(--bar)"/>
    <path d="M18 56 55 52 90 54 120 52 150 50 175 52V56z" fill="#7389a8"/>
    <path d="M18 56H175" stroke="#999" stroke-width=".4"/>
    <g class="axis" text-anchor="middle" style="font-size:3.4px"><text x="24" y="62">Category 1</text><text x="55" y="62">Category 2</text><text x="90" y="62">Category 3</text><text x="125" y="62">Category 4</text><text x="162" y="62">Category 5</text></g>
    <text x="18" y="72" class="axis" style="font-size:3.4px"><tspan font-weight="700">Source</tspan> Corvane 26/05/2011</text>
  </svg>
  <div class="band-head" style="left:10px;top:133px;width:188px">Some title here</div>
  <div class="band-head" style="left:200px;top:133px;width:188px">Some title here</div>
  <svg style="position:absolute;left:14px;top:150px" width="180" height="88" viewBox="0 0 180 88">
    <g class="axis" text-anchor="end" style="font-size:3.6px"><text x="20" y="8">May</text><text x="20" y="25">Apr</text><text x="20" y="42">Mar</text><text x="20" y="59">Feb</text><text x="20" y="76">Jan</text></g>
    <g fill="var(--bar-soft)"><rect x="24" y="2" width="135" height="3"/><rect x="24" y="19" width="90" height="3"/><rect x="24" y="36" width="140" height="3"/><rect x="24" y="53" width="120" height="3"/><rect x="24" y="70" width="135" height="3"/></g>
    <g fill="var(--bar)"><rect x="24" y="6" width="140" height="4"/><rect x="24" y="23" width="140" height="4"/><rect x="24" y="40" width="75" height="4"/><rect x="24" y="57" width="135" height="4"/><rect x="24" y="74" width="140" height="4"/></g>
    <g class="axis" style="font-size:3.2px"><text x="161" y="5">90</text><text x="166" y="10">100</text><text x="116" y="22">60</text><text x="166" y="27">100</text><text x="166" y="39">100</text><text x="101" y="44">50</text><text x="146" y="56">80</text><text x="161" y="61">90</text><text x="161" y="73">90</text><text x="166" y="78">100</text></g>
    <text x="24" y="86" class="axis" style="font-size:3.4px"><tspan font-weight="700">Source</tspan> Corvane 26/05/2011</text>
  </svg>
  <svg style="position:absolute;left:205px;top:150px" width="180" height="88" viewBox="0 0 180 88">
    <g class="axis" text-anchor="end" style="font-size:3.4px"><text x="22" y="12">Category 4</text><text x="22" y="30">Category 3</text><text x="22" y="48">Category 2</text><text x="22" y="66">Category 1</text></g>
    <path d="M26 2V74" stroke="#ccc" stroke-width=".4"/>
    <rect x="26" y="8" width="146" height="6" fill="#a6d58c"/>
    <rect x="26" y="26" width="90" height="6" fill="#dfe59f"/>
    <rect x="26" y="44" width="38" height="6" fill="#f6d98c"/>
    <rect x="26" y="62" width="66" height="6" fill="#f6c9c6"/>
    <g class="axis" text-anchor="middle" style="font-size:3.2px"><text x="26" y="79">0%</text><text x="40.6" y="79">10%</text><text x="55.2" y="79">20%</text><text x="69.8" y="79">30%</text><text x="84.4" y="79">40%</text><text x="99" y="79">50%</text><text x="113.6" y="79">60%</text><text x="128.2" y="79">70%</text><text x="142.8" y="79">80%</text><text x="157.4" y="79">90%</text><text x="172" y="79">100%</text></g>
    <text x="4" y="86" class="axis" style="font-size:3.4px"><tspan font-weight="700">Source</tspan> Corvane 26/05/2011</text>
  </svg>
  <div class="footer-mark"><i></i>CORVANE</div>
</section>

<!-- 9 Team structure -->
<section class="slide c3 r3">
  <h1 class="slide-title">Team Structure</h1>
  <p class="slide-sub">Maecenas sem eros, luctus quis facilisis in, tristique sit amet erat.</p>
  <div class="page-no">9</div>
  <div class="board">
    <h5>Defence Committee of the Board</h5>
    <table>
      <tr><td style="vertical-align:middle">Composition</td><td>Key board member<br>Non-executive representative<br>Company Secretary</td></tr>
      <tr><td>Key tasks</td><td>To initiate and handle a defence and related negotiations</td></tr>
    </table>
  </div>
  <div class="task-head">KEY TASK OF THE DEFENCE ADVISORY GROUP</div>
  <div class="team">
    <div><h6>CORVANE</h6><ul><li>Strategic and tactical advice on the conduct of the defence</li><li>Valuation</li><li>Negotiation</li><li>Critique of offeror</li><li>Analysis of possible the white knights</li><li>Black book preparation</li><li>Advice on "standards of care"</li><li>Liaising with Panel</li><li>Project management</li></ul></div>
    <div><h6>BROKERS</h6><ul><li>Strategic and tactical advice on the conduct of the defence</li><li>Investor relations</li><li>Monitoring market developments</li><li>Daily record of share dealings</li><li>Maintaining contact with key institutional shareholders</li><li>Advice on market reaction to defence story</li><li>Critique of offeror</li></ul></div>
    <div><h6>LAWYERS</h6><ul><li>General legal advice in relation to bid</li><li>Guidance on submissions to competition and other authorities</li><li>Providing input to defence documents</li><li>Other legal/ regulatory issues</li></ul></div>
    <div><h6>ACCOUNTANTS</h6><ul><li>Assisting in preparation of profit forecasts and asset valuations</li><li>Confirming the accuracy of financial information</li><li>Forensic analysis of bidders accounts/policies</li></ul></div>
    <div><h6>PR</h6><ul><li>Liaising with key journalists/analysts</li><li>Identification of people of influence</li><li>Assisting broker in shareholder communications</li><li>"Opinion polls"</li><li>Circulate daily press cuttings, obtaining and circulating documents</li><li>Assisting in preparation of letters to employees</li><li>Assisting in conducting internal staff briefings</li></ul></div>
  </div>
  <div class="footer-mark"><i></i>CORVANE</div>
</section>

</body>
</html>
```